Lumo4Kart - a fintech company - business card

We need a business card design for our Payments Technology company in Sydney, Australia. We provide business with payment solutions expanding across EFTPOS machines, online payment gateways and mobile payment solutions. We would like to see designs that are clean, classy and professional.
Target Market(s)
Business professionals, executives, c-suite
Industry/Entity Type
Fintech
Contact Information for Business Card
Will be on 400gsm. Logo will most likely be spot gloss unless designer recommends otherwise.
Font styles to use
Sans Serif
Requirements
Must have
- We need our website (lumo4kart.com.au), email (contact@lumo4kart.com.au), mobile (0432 587 904) and direct phone number (02 6815 3927) to feature on the card along with our logo (attached) and the words "EFTPOS | ONLINE | MOBILE"
- Font = Roboto

```html
<!DOCTYPE html>
<html lang="en">
<head>
<meta charset="UTF-8">
<title>Lumo4Kart – Business Card</title>
<link rel="stylesheet" href="https://fonts.googleapis.com/css2?family=Roboto:wght@400;700;900&family=Roboto+Condensed:wght@700&display=swap">
<style>
  :root {
    --bg: #e9eaec;
    --navy: #0f4f7f;
    --blue: #135e93;
    --blue-soft: #1a6aa3;
    --blue-bright: #1f7bbd;
    --paper: #ffffff;
    --paper-shade: #eeeff1;
    --ink: #2f3338;
    --grey-name: #5c5f63;
    --rule: #8a8d91;
  }
  * { margin: 0; padding: 0; box-sizing: border-box; }
  html, body { width: 1200px; height: 882px; overflow: hidden; }
  body {
    background: var(--bg);
    font-family: "Roboto", Arial, sans-serif;
    position: relative;
  }
  .card {
    position: absolute;
    top: 163px;
    width: 340px;
    height: 556px;
    overflow: hidden;
    box-shadow: 0 10px 28px rgba(0, 0, 0, 0.18);
  }

  /* Front */
  .card--front {
    left: 220px;
    background: linear-gradient(160deg, var(--blue-soft) 0%, var(--blue) 45%, var(--navy) 100%);
    color: var(--paper);
  }
  .card--front .brand {
    position: absolute;
    top: 210px;
    left: 0;
    right: 0;
    display: flex;
    flex-direction: column;
    align-items: center;
  }
  .brand__dot {
    width: 86px;
    height: 86px;
    border-radius: 50%;
    background: var(--paper);
    margin-bottom: 18px;
  }
  .brand__name {
    font-weight: 900;
    font-size: 38px;
    letter-spacing: 0.5px;
    line-height: 1;
  }
  .services {
    margin-top: 22px;
    font-family: "Roboto Condensed", "Roboto", sans-serif;
    font-weight: 700;
    font-size: 17px;
    letter-spacing: 1px;
  }
  .services .sep { font-weight: 400; opacity: 0.85; margin: 0 4px; }

  /* Back */
  .card--back {
    left: 660px;
    background: radial-gradient(circle at 50% 30%, var(--paper) 0%, var(--paper) 40%, var(--paper-shade) 100%);
    color: var(--ink);
  }
  .card--back .brand {
    position: absolute;
    top: 72px;
    left: 0;
    right: 0;
    display: flex;
    flex-direction: column;
    align-items: center;
  }
  .card--back .brand__dot {
    width: 70px;
    height: 70px;
    background: var(--blue);
    margin-bottom: 14px;
  }
  .card--back .brand__name {
    color: var(--grey-name);
    font-size: 30px;
  }
  .contacts {
    position: absolute;
    top: 218px;
    left: 48px;
    right: 40px;
    list-style: none;
  }
  .contacts li {
    display: flex;
    align-items: center;
    gap: 12px;
    height: 36px;
    border-bottom: 1px dotted var(--rule);
    font-size: 14px;
  }
  .contacts .web { color: var(--ink); }
  .contacts .web span { color: var(--blue-bright); }
  .icon {
    width: 20px;
    height: 20px;
    flex: none;
  }
  .back-band {
    position: absolute;
    left: 0;
    right: 0;
    bottom: 0;
    height: 150px;
    background: linear-gradient(180deg, rgba(19, 94, 147, 0) 0%, var(--blue) 35%, var(--navy) 100%);
  }
</style>
</head>
<body>

  <section class="card card--front" aria-label="Card front">
    <div class="brand">
      <div class="brand__dot"></div>
      <div class="brand__name">LUMO4KART</div>
      <div class="services">EFTPOS<span class="sep">|</span>ONLINE<span class="sep">|</span>MOBILE</div>
    </div>
  </section>

  <section class="card card--back" aria-label="Card back">
    <div class="brand">
      <div class="brand__dot"></div>
      <div class="brand__name">LUMO4KART</div>
    </div>

    <ul class="contacts">
      <li>
        <svg class="icon" viewBox="0 0 20 20" aria-hidden="true">
          <circle cx="10" cy="10" r="10" fill="var(--blue)"/>
          <rect x="7" y="4.5" width="6" height="11" rx="1" fill="none" stroke="#fff" stroke-width="1.4"/>
          <circle cx="10" cy="13.4" r="0.7" fill="#fff"/>
        </svg>
        <span>0432 587 904</span>
      </li>
      <li>
        <svg class="icon" viewBox="0 0 20 20" aria-hidden="true">
          <circle cx="10" cy="10" r="10" fill="var(--blue)"/>
          <path d="M7 5.2l1.8-0.4 1 2.4-1.2 0.9c0.6 1.4 1.5 2.3 2.9 2.9l0.9-1.2 2.4 1-0.4 1.8c-3.9 0.2-7.6-3.5-7.4-7.4z" fill="#fff"/>
        </svg>
        <span>02 6815 3927</span>
      </li>
      <li>
        <svg class="icon" viewBox="0 0 20 20" aria-hidden="true">
          <circle cx="10" cy="10" r="10" fill="var(--blue)"/>
          <rect x="5" y="6.5" width="10" height="7" rx="0.8" fill="#fff"/>
          <path d="M5.3 7l4.7 3.6L14.7 7" fill="none" stroke="var(--blue)" stroke-width="1"/>
        </svg>
        <span>contact@lumo4kart.com.au</span>
      </li>
      <li>
        <svg class="icon" viewBox="0 0 20 20" aria-hidden="true">
          <circle cx="10" cy="10" r="10" fill="var(--blue)"/>
          <g fill="none" stroke="#fff" stroke-width="1">
            <circle cx="10" cy="10" r="5"/>
            <ellipse cx="10" cy="10" rx="2.2" ry="5"/>
            <path d="M5 10h10M6 7.3h8M6 12.7h8"/>
          </g>
        </svg>
        <span class="web">www.<span>lumo4kart.com.au</span></span>
      </li>
    </ul>

    <div class="back-band" role="img" aria-label="Decorative blue wave band along the bottom of the card"></div>
  </section>

</body>
</html>
```